R&t Subterra

We specialize in CIPP pipe lining but do other underground utilities trenchless as well.

Target Market(s)

Trenchless sewer replacement

Contact Information for Business Card

Gavin Holtby 715-482-6130 Wisconsin rapids, wi

```html
<!DOCTYPE html>
<html lang="en">
<head>
<meta charset="utf-8">
<title>R&amp;t Subterra — Business Card</title>
<link rel="stylesheet" href="https://fonts.googleapis.com/css2?family=Poppins:wght@500;600;700&display=swap">
<style>
  :root {
    --page: #e4e6e8;
    --card: #ffffff;
    --blue: #3590cf;
    --blue-light: #58b0e3;
    --grey: #a9a9ab;
    --grey-line: #c9c9cb;
    --white: #ffffff;
  }
  * { margin: 0; padding: 0; box-sizing: border-box; }
  html, body { width: 1200px; height: 1200px; overflow: hidden; }
  body { background: var(--page); font-family: "Poppins", sans-serif; position: relative; }

  .card {
    position: absolute; left: 175px; width: 853px; height: 472px;
    background: var(--card); overflow: hidden;
    box-shadow: 0 18px 30px rgba(0,0,0,0.18);
  }
  .card--front { top: 62px; }
  .card--back { top: 629px; }

  .brand { position: absolute; display: flex; align-items: center; }
  .brand__dot { border-radius: 50%; background: var(--grey); flex: none; }
  .brand__name { color: var(--blue); font-weight: 700; line-height: 1; white-space: nowrap; }

  .card--front .brand { left: 162px; top: 75px; gap: 24px; }
  .card--front .brand__dot { width: 112px; height: 112px; }
  .card--front .brand__name { font-size: 72px; }

  .contact-band {
    position: absolute; left: 0; top: 244px; width: 100%; height: 68px;
    background: var(--grey); display: flex; align-items: center; padding-left: 40px;
  }
  .contact-item { display: flex; align-items: center; color: var(--white); font-weight: 600; white-space: nowrap; }
  .icon { flex: none; }
  .contact-item--phone { font-size: 31px; gap: 18px; margin-right: 28px; letter-spacing: 0.5px; }
  .contact-item--web { font-size: 20px; gap: 14px; }

  .brand-decoration {
    position: absolute; left: 0; top: 312px; width: 100%; height: 160px;
    background: linear-gradient(90deg, var(--blue) 0%, var(--blue-light) 100%);
  }

  .brand-panel {
    position: absolute; left: 0; top: 0; width: 325px; height: 100%;
    background: linear-gradient(160deg, var(--blue-light) 0%, var(--blue) 100%);
  }
  .card--back .brand { left: 381px; top: 114px; gap: 18px; }
  .card--back .brand__dot { width: 90px; height: 90px; }
  .card--back .brand__name { font-size: 46px; }

  .info-band {
    position: absolute; left: 375px; right: 0; top: 280px; height: 156px;
    background: var(--blue); padding: 8px 0 0 16px;
    display: flex; flex-direction: column; gap: 6px;
  }
  .info-band .contact-item--phone { font-size: 36px; gap: 24px; margin: 0; line-height: 1.25; }
  .info-band .contact-item--web { font-size: 19px; gap: 24px; }
  .address-row { display: flex; align-items: center; gap: 24px; color: var(--white); font-weight: 600; font-size: 18px; }
  .address-line { width: 340px; border-bottom: 3px dotted var(--white); padding-bottom: 2px; white-space: nowrap; }

  .footer-rule { position: absolute; left: 200px; right: 0; height: 5px; background: var(--grey-line); }
  .footer-rule--one { top: 446px; }
  .footer-rule--two { top: 459px; }
</style>
</head>
<body>

<section class="card card--front">
  <div class="brand">
    <span class="brand__dot"></span>
    <span class="brand__name">R&amp;t Subterra</span>
  </div>

  <div class="contact-band">
    <div class="contact-item contact-item--phone">
      <svg class="icon" width="38" height="38" viewBox="0 0 38 38"><circle cx="19" cy="19" r="19" fill="#3590cf"/><path d="M13 10c1.5-1 2.5 0 3.5 2l1 2c.5 1 0 2-1 2.5-.6.4-.6 1 0 2l2.5 3c.7.8 1.3.8 2 .2 1-1 2-1.2 3-.4l2 1.5c1.3 1 1.2 2.2 0 3.4-2 2-5 1.5-8.5-1.5S10.5 17 11 13.5c.3-1.6 1-2.8 2-3.5z" fill="#fff"/></svg>
      <span>715 - 482 - 6130</span>
    </div>
    <div class="contact-item contact-item--web">
      <svg class="icon" width="36" height="36" viewBox="0 0 36 36" fill="none" stroke="#3590cf" stroke-width="2.4"><circle cx="16" cy="16" r="13"/><ellipse cx="16" cy="16" rx="6" ry="13"/><path d="M3 16h26M5 9h22M5 23h22"/><path d="M24 22l9 4-4 1.5-1.5 4z" fill="#3590cf"/></svg>
      <span>www.rtsubterra.com</span>
    </div>
  </div>

  <div class="brand-decoration" role="img" aria-label="Large blue decorative company lettering"></div>
</section>

<section class="card card--back">
  <div class="brand-panel" role="img" aria-label="Enlarged blue company symbol as decoration"></div>

  <div class="brand">
    <span class="brand__dot"></span>
    <span class="brand__name">R&amp;t Subterra</span>
  </div>

  <div class="info-band">
    <div class="contact-item contact-item--phone">
      <svg class="icon" width="38" height="38" viewBox="0 0 38 38"><circle cx="19" cy="19" r="19" fill="#fff"/><path d="M13 10c1.5-1 2.5 0 3.5 2l1 2c.5 1 0 2-1 2.5-.6.4-.6 1 0 2l2.5 3c.7.8 1.3.8 2 .2 1-1 2-1.2 3-.4l2 1.5c1.3 1 1.2 2.2 0 3.4-2 2-5 1.5-8.5-1.5S10.5 17 11 13.5c.3-1.6 1-2.8 2-3.5z" fill="#3590cf"/></svg>
      <span>715 - 482 - 6130</span>
    </div>
    <div class="contact-item contact-item--web">
      <svg class="icon" width="38" height="38" viewBox="0 0 36 36" fill="none" stroke="#fff" stroke-width="2.4"><circle cx="16" cy="16" r="13"/><ellipse cx="16" cy="16" rx="6" ry="13"/><path d="M3 16h26M5 9h22M5 23h22"/><path d="M24 22l9 4-4 1.5-1.5 4z" fill="#fff"/></svg>
      <span>www.rtsubterra.com</span>
    </div>
    <div class="address-row">
      <svg class="icon" width="38" height="40" viewBox="0 0 38 40"><path d="M19 3c-6 0-10 4.5-10 10 0 7 10 18 10 18s10-11 10-18c0-5.5-4-10-10-10z" fill="none" stroke="#fff" stroke-width="2.6"/><circle cx="19" cy="13" r="3.5" fill="#fff"/><path d="M11 35h16" stroke="#fff" stroke-width="2.6"/></svg>
      <span class="address-line">Wisconsin Rapids, WI</span>
    </div>
  </div>

  <div class="footer-rule footer-rule--one"></div>
  <div class="footer-rule footer-rule--two"></div>
</section>

</body>
</html>
```